Logo needed for business card

Velistra Pty Ltd is in the business of healthcare and ecommerce.

We own and manage pharmacies and online health ecomerce sites.

We provide ecommerce consultants for companies looking for an ecommerce business startegy.

Think of it as the umbrella under which several healthcare brands may sit.

When I think of Velistra, I visulaise slick black/metalic colours, so please stay away from the common blue and green colours that seem to be so popular in this field.

Target Market(s)

CEOs and COOs

Industry/Entity Type

Healthcare

Contact Information for Business Card

Delphine Okoro
Director
Velistra Pty Ltd
4/237 Kelburn Pde
Kelmont, NSW 2041

Requirements
Must have
• Design must have scope to be implemented on the company's website and letterheads etc.

```html
<!DOCTYPE html>
<html lang="en">
<head>
<meta charset="utf-8">
<title>Velistra Pty Ltd – Business Card</title>
<link href="https://fonts.googleapis.com/css2?family=Arimo:ital,wght@0,400;0,700;1,700&display=swap" rel="stylesheet">
<style>
  :root {
    --stage: #3b3d40;
    --card-light: #ffffff;
    --card-shade: #d9d9d9;
    --gold: #c9a24a;
    --gold-pale: #f4df9e;
    --ink: #111111;
    --label: #ffffff;
  }
  * { margin: 0; padding: 0; box-sizing: border-box; }
  html, body {
    width: 1200px;
    height: 646px;
    overflow: hidden;
    background: var(--stage);
    font-family: "Arimo", Arial, sans-serif;
  }
  .business-card {
    position: absolute;
    left: 100px;
    top: 37px;
    width: 1000px;
    height: 572px;
    overflow: hidden;
    border-radius: 4px;
    box-shadow: 0 10px 30px rgba(0,0,0,0.35);
  }
  .card-backdrop {
    position: absolute;
    inset: 0;
    width: 100%;
    height: 100%;
  }
  .brand {
    position: absolute;
    left: 80px;
    top: 300px;
    display: flex;
    align-items: center;
    gap: 22px;
  }
  .brand-dot {
    width: 58px;
    height: 58px;
    border-radius: 50%;
    background: var(--gold);
  }
  .brand-name {
    font-weight: 700;
    font-size: 104px;
    letter-spacing: -2px;
    color: var(--ink);
    line-height: 1;
  }
  .contact {
    position: absolute;
    right: 50px;
    top: 62px;
    width: 470px;
  }
  .person {
    display: flex;
    align-items: baseline;
    justify-content: flex-end;
    gap: 14px;
  }
  .person-first,
  .person-last {
    font-weight: 700;
    font-size: 46px;
  }
  .person-first { color: var(--ink); }
  .person-last { color: var(--gold); }
  .role {
    text-align: right;
    font-weight: 700;
    font-size: 17px;
    letter-spacing: 1px;
    color: var(--ink);
    margin-top: 2px;
  }
  .label {
    background: var(--label);
    box-shadow: 0 1px 3px rgba(0,0,0,0.12);
    margin-left: 40px;
  }
  .company {
    margin-top: 34px;
    padding: 10px 18px;
    font-weight: 700;
    font-style: italic;
    font-size: 19px;
    letter-spacing: 1px;
    color: var(--ink);
  }
  .address {
    margin-top: 18px;
    padding: 12px 18px;
    font-weight: 700;
    font-size: 19px;
    line-height: 1.3;
    color: var(--ink);
  }
</style>
</head>
<body>
  <article class="business-card">
    <svg class="card-backdrop" viewBox="0 0 1000 572" preserveAspectRatio="none" aria-hidden="true">
      <defs>
        <linearGradient id="cardSurface" x1="0" y1="0" x2="1" y2="1">
          <stop offset="0" stop-color="var(--card-shade)"/>
          <stop offset="0.45" stop-color="var(--card-light)"/>
          <stop offset="1" stop-color="#ececec"/>
        </linearGradient>
        <linearGradient id="goldWave" x1="0" y1="0" x2="1" y2="1">
          <stop offset="0" stop-color="#f7e7b4"/>
          <stop offset="1" stop-color="var(--gold-pale)"/>
        </linearGradient>
      </defs>
      <rect class="surface" width="1000" height="572" fill="url(#cardSurface)"/>
      <path class="wave-fill" d="M250 572 C 520 560, 700 470, 800 330 C 870 230, 920 160, 1000 130 L1000 572 Z" fill="url(#goldWave)"/>
      <path class="wave-line" d="M250 572 C 520 560, 700 470, 800 330 C 870 230, 920 160, 1000 130" fill="none" stroke="var(--ink)" stroke-width="6"/>
      <path class="under-line" d="M170 572 C 420 548, 620 470, 720 360" fill="none" stroke="#9a9a9a" stroke-width="3" opacity="0.6"/>
    </svg>

    <div class="brand">
      <span class="brand-dot"></span>
      <span class="brand-name">Velistra</span>
    </div>

    <div class="contact">
      <div class="person">
        <span class="person-first">Delphine</span>
        <span class="person-last">Okoro</span>
      </div>
      <div class="role">DIRECTOR</div>
      <div class="label company">VELISTRA PTY LTD</div>
      <div class="label address">4/237 Kelburn Pde Kelmont,<br>NSW 2041</div>
    </div>
  </article>
</body>
</html>
```